Smart, intuitive SaaS software dashboard design

PactBloom is an innovative modern SaaS (software as a service) solution for contract and meeting management.

What we are looking for is fresh ideas for our dashboard. We do not need web coding or actionable wireframes now – but purely great design ideas from where to continue forward.

How should a modern web software dashboard look like? Fresh, intuitive, easy-to-use, and adaptable for responsive mobile designs. We hope that when the user logs into the service and sees the dashboard, he/she gets a good big picture of the current status of the most important documents of his/hers company.

To get to know the service and see the components, we kindly ask you to register to our service at www.pactbloom-demo.net and to utilize the free trial (30 days) so you can see the existing dashboard live. And also try out how it works. Might help you to get ideas how to improve it.

(The designer we will choose might be offered later on to design some other pages as well (contract view and edit pages, meeting page etc).)

You’ll find additional information in the attachment.

You’ll find more information of the company and the service also at www.pactbloom-demo.net

Target Market(s)

Global

Industry/Entity Type

Business Management

Number of Pages Required

1 page

Font styles to use
Sans Serif

Requirements
Must have
• 1) Clear design idea for us to iterate from, 2) Modern look and feel - elegant & bold at the same time - still with credibility in our target group. And 3) Suitable for dashboard usage - it should it a clear big picture for the user.
• UPDATE:
• Users should see most important things with one glance. Therefore we would like to see AT LEAST these items mentioned below on the first page.
• NOTE: if all these things are visible on the dashboard, the menu list is maybe not needed on the left. (And there might be some icons on the top header with needed settings/inbox features anyway.)
• NOTE2: as explained earlier, the design should be responsive i.e. work without modifications in PC, iPad and mobile (the areas/boxes would just rearrange themselves on top of each other.)
• -First area should be Documents, which would include different document categories: Contracts, Finance & Admin and HR
• -All different types of Meetings could be the next area (upcoming ones clearly visible with date and maybe description, time and location visible also).
• -Reminders and Activity Feed (they might also be together in top of each other, so that Reminder is visible first and Activity feed can be chosen from the tab.)
• -Virtual Datarooms (maybe 1-3 different ones with some analytics for each visible e.g. like usage/visits per day)
• Saved searches in very important list as users can save their most important searches. There are typically many of these, so at least 5 should be visible and then see all button (maybe even more could be visible if they fit on your design)
• My Latest is also important.
• (As explained, Action Required area is NOT needed anymore).
Nice to have
• Surprise us!
Should not have
• Please avoid the boring traditional legacy stuff and the common report dashboards.
• You do not need design a 100% mockup for the techie to continue with. The ideas count.

```html
<!DOCTYPE html>
<html lang="en">
<head>
<meta charset="utf-8">
<title>PactBloom Dashboard</title>
<link href="https://fonts.googleapis.com/css2?family=Quicksand:wght@400;500;600&family=Cabin:wght@400;500;600&display=swap" rel="stylesheet">
<style>
:root{
  --bar:#3a3a3c;
  --bar-line:#4d4d50;
  --side:#6b6b6d;
  --side-sub:#505052;
  --head:#3b3b3e;
  --green:#3aad49;
  --green-bright:#5fd14a;
  --blue:#2e8fe0;
  --panel:#5a5a5e;
  --panel-head:#9c9c9e;
  --meet:#555558;
  --brown:#4a4440;
  --white:#ffffff;
  --muted:#d8d8d8;
}
*{margin:0;padding:0;box-sizing:border-box}
html,body{width:1200px;height:900px;overflow:hidden}
body{position:relative;font-family:"Quicksand",sans-serif;color:var(--white);background:#555}
.backdrop{position:absolute;left:152px;top:184px;width:1048px;height:716px;
  background:linear-gradient(180deg,#b9bdbf 0%,#a7a9a6 18%,#8b8576 38%,#6d6656 55%,#4d473d 75%,#33302b 100%)}
.topbar{position:absolute;left:0;top:0;width:1200px;height:42px;background:var(--bar);display:flex;align-items:center}
.topbar .icon-cell{width:51px;height:42px;border-right:1px solid var(--bar-line);display:flex;align-items:center;justify-content:center;position:relative}
.badge{position:absolute;top:3px;right:9px;width:14px;height:14px;border-radius:50%;background:#e53935;font-size:9px;font-weight:600;display:flex;align-items:center;justify-content:center;font-family:"Cabin",sans-serif}
.login-note{margin-left:10px;font-family:"Cabin",sans-serif;font-size:10px;color:#ddd;white-space:nowrap}
.brand{position:absolute;left:508px;top:8px;display:flex;align-items:center;gap:6px;font-size:17px;font-weight:600;letter-spacing:.5px;color:var(--white)}
.brand .dot{width:20px;height:20px;border-radius:50%;background:var(--green)}
.search{position:absolute;left:702px;top:8px;width:356px;height:25px;border-radius:4px;background:#d6d6d6;color:#555;font-size:14px;padding:3px 14px;font-style:italic}
.search svg{position:absolute;right:10px;top:4px}
.gear{position:absolute;right:0;top:0;width:50px;height:42px;background:#4a4a4d;display:flex;align-items:center;justify-content:center}
.sidebar{position:absolute;left:0;top:42px;width:152px;height:858px;background:linear-gradient(180deg,#727274,#5c5c5e)}
.nav a{display:block;height:35px;line-height:35px;padding-left:20px;font-size:12.5px;color:var(--white);text-decoration:none;font-weight:500;white-space:nowrap;letter-spacing:-.1px}
.nav .active{border-right:3px solid var(--green)}
.nav .sub{background:var(--side-sub);padding:2px 0}
.nav .sub a{padding-left:35px;height:29.3px;line-height:29.3px}
.upgrade{position:absolute;left:44px;width:50px;text-align:center;font-size:11px;font-family:"Cabin",sans-serif}
.upgrade .gem{width:32px;height:32px;margin:0 auto 4px;border-radius:50%;background:var(--green);position:relative}
.upgrade .gem span{position:absolute;right:-10px;top:-8px;width:18px;height:18px;border-radius:50%;background:#2f5d34;font-size:11px;line-height:18px}
.hero{position:absolute;left:152px;top:42px;width:1048px;height:142px;background:var(--head)}
.avatar{position:absolute;left:14px;top:25px;width:88px;height:84px;border-radius:50%;background:radial-gradient(circle at 50% 40%,#6b4a35,#2e2620)}
.hero h1{position:absolute;left:121px;top:31px;font-size:17px;font-weight:500}
.hero .welcome{position:absolute;left:126px;top:66px;font-size:12px;font-weight:400;line-height:19px;font-family:"Cabin",sans-serif;white-space:nowrap}
.hero .welcome small{font-size:10.5px;display:block;line-height:18px;font-weight:400}
.stat{position:absolute;top:34px;text-align:center;width:140px}
.stat b{display:block;font-size:52px;font-weight:400;line-height:52px}
.stat span{font-size:14px;font-weight:500}
.profile-menu{position:absolute;left:1074px;top:42px;width:126px;height:90px;background:#58585b;font-size:12px;color:#ddd;padding:14px 0 0 8px}
.profile-menu div{display:flex;align-items:center;gap:6px;height:35px}
.pin-tab{position:absolute;left:1162px;top:230px;width:38px;height:40px;background:var(--green);display:flex;align-items:center;justify-content:center}
.glance-title{position:absolute;left:172px;top:197px;font-size:29px;color:#6a6a6c;font-weight:400}
.chart-card{position:absolute;left:163px;top:237px;width:471px;height:246px;background:var(--panel)}
.chart-card header{height:45px;background:var(--panel-head);display:flex;align-items:center;padding-left:18px;gap:12px;font-size:12.5px;font-weight:500}
.meet-card{position:absolute;left:723px;top:237px;width:315px;height:268px;background:var(--meet);font-family:"Cabin",sans-serif;padding:0 20px}
.meet-card .row1{display:flex;justify-content:space-between;align-items:center;height:52px;font-size:12px}
.meet-card .row1 small{font-size:8.5px}
.month{height:26px;background:#fff;border-radius:2px;display:flex;color:#333;font-size:9.5px;font-weight:600}
.month span{display:flex;align-items:center;justify-content:center}
.total{margin-top:22px;font-size:13px}
.progress{margin-top:8px;height:3px;background:#e8e8e8}
.progress i{display:block;width:79%;height:100%;background:var(--green)}
.meta{margin-top:14px;font-size:10px;line-height:22.5px}
.meta b{display:inline-block;width:73px;font-weight:500}
.meta span{color:#ddd}
.meet-actions{display:flex;justify-content:space-between;margin-top:8px}
.meet-actions a{height:26px;width:119px;display:flex;align-items:center;justify-content:center;gap:8px;font-size:10px;font-weight:600;color:#fff;text-decoration:none}
.actions-band{position:absolute;left:168px;top:511px;width:990px;height:129px;background:rgba(80,72,66,.55)}
.big-btn{position:absolute;top:46px;width:269px;height:40px;background:var(--green);color:#fff;font-size:23px;font-weight:500;display:flex;align-items:center;justify-content:center;text-decoration:none}
.alerts{position:absolute;left:166px;top:654px;width:541px;height:230px}
.alerts header,.latest header{height:42px;background:var(--brown);display:flex;align-items:center;font-size:14px;font-weight:500}
.alerts header{padding-left:22px;gap:14px}
.alert{height:62px;background:rgba(55,50,45,.55);border-bottom:1px solid rgba(255,255,255,.08);display:flex;align-items:center;justify-content:space-between;padding:0 22px;font-size:12.5px;font-weight:500}
.alert.dim{color:#d0d0d0;padding-top:14px}
.latest{position:absolute;left:715px;top:654px;width:441px;height:230px}
.latest header{justify-content:center;font-family:"Cabin",sans-serif;font-weight:500;font-size:13px}
.latest .body{height:188px;background:#2f2a26;padding:8px 26px 0 25px;font-size:12px;line-height:22.4px;position:relative;overflow:hidden}
.latest .body p+p{margin-top:19px}
.latest .scroll{position:absolute;right:4px;top:6px;width:4px;height:180px;background:#3c3732}
.latest .scroll i{display:block;height:68px;margin-top:34px;background:#6a625a}
</style>
</head>
<body>
<div class="backdrop" role="img" aria-label="Blurred landscape photo of grassy dunes under an overcast sky"></div>

<div class="topbar">
  <div class="icon-cell"><svg width="20" height="20" viewBox="0 0 20 20" fill="none" stroke="#fff" stroke-width="1.8"><circle cx="10" cy="10" r="8"/><path d="M10 5v5h3"/></svg></div>
  <div class="icon-cell"><svg width="20" height="20" viewBox="0 0 20 20" fill="none" stroke="#fff" stroke-width="1.8"><circle cx="10" cy="10" r="8"/><path d="M10 5v6"/><circle cx="10" cy="14" r=".6" fill="#fff"/></svg></div>
  <div class="icon-cell"><svg width="22" height="16" viewBox="0 0 22 16" fill="none" stroke="#fff" stroke-width="1.6"><rect x="1" y="1" width="20" height="14"/><path d="M1 1l10 8 10-8"/></svg><span class="badge">2</span></div>
  <div class="login-note">Mr. Dean Parker, you are logged in to your account.</div>
  <div class="brand"><span class="dot"></span>PactBloom</div>
  <div class="search">Search Contract<svg width="18" height="18" viewBox="0 0 18 18" fill="none" stroke="#444" stroke-width="2"><circle cx="7.5" cy="7.5" r="6"/><path d="M12 12l5 5"/></svg></div>
  <div class="gear"><svg width="20" height="20" viewBox="0 0 20 20"><circle cx="10" cy="10" r="6.5" fill="none" stroke="#888" stroke-width="3" stroke-dasharray="3 2"/><circle cx="10" cy="10" r="3" fill="none" stroke="#888" stroke-width="2"/></svg></div>
</div>

<aside class="sidebar">
  <nav class="nav" style="margin-top:20px">
    <a class="active">Dashboard</a>
    <a>Contracts</a>
    <a>HR</a>
    <a>Finance &amp; Admin</a>
    <div class="sub"><a>My Finance</a><a>Finance</a><a>Finnance</a><a>Finance</a></div>
    <a>Board Meeting</a>
    <a>Shareholders Meeting</a>
    <a>Other Meetings</a>
    <a>Company Register</a>
    <a>Saved Searches</a>
    <a>Settings</a>
  </nav>
  <div class="upgrade" style="top:786px"><div class="gem"><span>2</span></div>Upgrade</div>
</aside>

<section class="hero">
  <div class="avatar" role="img" aria-label="Profile photo of the signed-in user"></div>
  <h1>Dashboard.</h1>
  <div class="welcome">Welcome to PactBloom<small>We've assembled some links to get you started:</small><small>Last login : 10-06-2016</small></div>
  <div class="stat" style="left:382px"><b>42</b><span>CONTRACTS</span></div>
  <div class="stat" style="left:564px"><b>3</b><span>MEETINGS</span></div>
  <div class="stat" style="left:735px"><b>17</b><span>PROJECTS</span></div>
</section>

<div class="profile-menu">
  <div><svg width="14" height="14" viewBox="0 0 14 14" fill="var(--green)"><circle cx="7" cy="4" r="3.5"/><path d="M0 14c0-4 3-6 7-6s7 2 7 6z"/></svg>Edit Profile</div>
  <div><svg width="14" height="14" viewBox="0 0 14 14" fill="none" stroke="var(--green)" stroke-width="1.5"><circle cx="7" cy="7" r="6"/><path d="M7 3.5v4"/></svg>Logout</div>
</div>

<div class="pin-tab"><svg width="14" height="16" viewBox="0 0 14 16" fill="none" stroke="#fff" stroke-width="3"><path d="M11 2L4 8l7 6"/></svg></div>

<h2 class="glance-title">At&nbsp; a Glance</h2>

<section class="chart-card">
  <header><svg width="16" height="16" viewBox="0 0 16 16" fill="#fff"><rect x="0" y="0" width="2" height="16"/><rect x="3" y="4" width="2" height="10"/><rect x="6" y="8" width="2" height="6"/><rect x="9" y="10" width="2" height="4"/><rect x="0" y="14" width="16" height="2"/></svg>Your Contracts so far...</header>
  <svg width="471" height="201" viewBox="0 0 471 201" font-family="Cabin, sans-serif" font-size="9.5" fill="#ddd">
    <g stroke="#2b2b2d" stroke-width="1">
      <line x1="48" y1="35" x2="471" y2="35"/><line x1="48" y1="66" x2="471" y2="66"/>
      <line x1="48" y1="94" x2="471" y2="94"/><line x1="48" y1="122" x2="471" y2="122"/>
      <line x1="48" y1="150" x2="471" y2="150"/>
    </g>
    <text x="12" y="34">1k +</text><text x="12" y="63">800 +</text><text x="12" y="92">500k +</text>
    <text x="12" y="121">100 +</text><text x="12" y="149">10+</text><text x="14" y="178">0</text>
    <g fill="#5c8f3c">
      <rect x="87" y="55" width="7" height="126"/><rect x="120" y="87" width="7" height="94"/>
      <rect x="153" y="137" width="7" height="44"/><rect x="186" y="30" width="7" height="151"/>
      <rect x="219" y="88" width="7" height="93"/>
    </g>
    <rect x="252" y="95" width="7" height="86" fill="var(--green-bright)"/>
    <g text-anchor="middle">
      <text x="90" y="193">Jan</text><text x="123" y="193">Feb</text><text x="156" y="193">Mar</text>
      <text x="189" y="193">Apr</text><text x="222" y="193">May</text><text x="256" y="193">Jun</text>
      <text x="288" y="193">Jul</text><text x="320" y="193">Aug</text><text x="354" y="193">Sep</text>
      <text x="387" y="193">Oct</text><text x="421" y="193">Nov</text><text x="455" y="193">Dec</text>
    </g>
  </svg>
</section>

<section class="meet-card">
  <div class="row1"><span>Meeting Reports</span><small>Show All</small></div>
  <div class="month">
    <span style="width:27px;border-right:1px solid #ddd;color:#bbb">◂</span>
    <span style="flex:1;justify-content:space-between;padding:0 12px">March 2015<em style="font-style:normal;color:#999">⌄</em></span>
    <span style="width:27px;border-left:1px solid #ddd;color:#bbb">▸</span>
  </div>
  <div class="total">700 Total Meetings</div>
  <div class="progress"><i></i></div>
  <div class="meta">
    <div><b>Release Date:</b><span>April 14th, 2015</span></div>
    <div><b>Reported by:</b><span>Liam Ford</span></div>
    <div><b>PDF Size:</b><span>13 MB</span></div>
  </div>
  <div class="meet-actions">
    <a style="background:var(--blue)"><svg width="12" height="12" viewBox="0 0 12 12" fill="none" stroke="#fff" stroke-width="1.3"><path d="M1 6a5 4 0 1 1 3 3.6L1 11z"/></svg>Send via Chat</a>
    <a style="background:var(--green)"><svg width="12" height="12" viewBox="0 0 12 12" fill="none" stroke="#fff" stroke-width="1.3"><path d="M6 1v7M3 5l3 3 3-3M1 9v2h10V9"/></svg>Download Report</a>
  </div>
</section>

<section class="actions-band">
  <a class="big-btn" style="left:19px">Schedule Meeting</a>
  <a class="big-btn" style="left:350px">New Contract</a>
  <a class="big-btn" style="left:696px">View Contract</a>
</section>

<section class="alerts">
  <header><svg width="20" height="20" viewBox="0 0 20 20" fill="none" stroke="#fff" stroke-width="1.4"><rect x="1" y="3" width="18" height="16"/><path d="M1 7h18M5 1v4M15 1v4"/><g fill="#fff" stroke="none"><rect x="4" y="9" width="2" height="2"/><rect x="8" y="9" width="2" height="2"/><rect x="12" y="9" width="2" height="2"/><rect x="4" y="13" width="2" height="2"/><rect x="8" y="13" width="2" height="2"/><rect x="12" y="13" width="2" height="2"/></g></svg>Alert Messages &amp; Notifications</header>
  <div class="alert" style="height:65px"><span>You have two upcoming meeting</span><svg width="20" height="20" viewBox="0 0 20 20" fill="none" stroke="#fff" stroke-width="1.6"><circle cx="10" cy="10" r="9"/><path d="M10 5v6"/><circle cx="10" cy="14.5" r=".6" fill="#fff"/></svg></div>
  <div class="alert dim"><span>You have two upcoming meeting</span><svg width="20" height="20" viewBox="0 0 20 20" fill="none" stroke="#fff" stroke-width="1.6" style="margin-top:-14px"><circle cx="10" cy="10" r="9"/><path d="M6 10l3 3 5-6"/></svg></div>
  <div class="alert dim"><span style="margin-top:14px">You have two upcoming meeting</span><svg width="20" height="20" viewBox="0 0 20 20" fill="none" stroke="#fff" stroke-width="1.6" style="margin-top:-14px"><circle cx="10" cy="10" r="9"/><path d="M7 7l6 6M13 7l-6 6"/></svg></div>
</section>

<section class="latest">
  <header>Latest Update</header>
  <div class="body">
    <p>Lorem ipsum dolor sit amet, consectetur adipisicing elit, sed do eius-mod tempor incididunt ut labore et dolore magna aliqua. Ut enim ad minim veniam, quis nostrud exercitation ullamco laboris nisi ut aliquip ex ea commodo consequat. Duis aute irure dolor in reprehenderit in</p>
    <p>Lorem ipsum dolor sit amet, consectetur adipisicing elit, sed do eius-mod tempor incididunt ut labore et dolore magna aliqua. Ut enim ad minim veniam, quis nostrud exercitation ullamco laboris nisi ut aliquip</p>
    <div class="scroll"><i></i></div>
  </div>
</section>
</body>
</html>
```